Ember Hollow Candles needs an elegant/eye catching packaging design

I need a packaging design for a medium sized candle. (Medium size package including dimensions is uploaded as file). I am going to launch my business next year. I will have 10 fragrances to choose from and have done my fragrance research and I will be to targeting the 25-35 year old market. The theme for this first range will be luxury/elegant candles. I have named my candles Ember Hollow Candles in admiration of this mystic mountain which is close to where I live in Murwillumbah called Tarrakoon (Mount Pellerby), whose local Aboriginal name translates to 'Ember Hollow'
Everyone refers to the mountain as the 'Ember Hollow'.
Mount Pellerby is the central volcanic remnant of an ancient shield volcano. Often when you look at it, it has clouds caught around it, is is just stunning, and breathtaking to look at! It can be seen from many points in Murwillumbah, its as if it is always watching you. Mount Pellerby is the central volcanic remnant of an ancient shield volcano. Lieutenant Henry Falstead saw the mountain from the sea and named it Mount Pellerby. Mount Pellerby was formed 23 milllion years ago and is the remnant central plug of the Orvel shelf volcano also know as the 'Orvel Basin' and is one of the largest and best examples of an erosion caldera in the world. it is also a sacred site to the Aboriginal Bundjalung people and its Aboriginal name is Tarrakoon. The mountain is now closed to climbers because it is a sacred site. As I will be doing several ranges of Candles, I want to start with a luxury candle to really pay respect to this mystical and stunning grand icon. I I will leave the design and colour to the designer to use their artistic flare but would like something mystical and elegant and eye catching. I do have two logos that I will be using which I have uploaded but the website needs to be added to one of the logos. The blue clouds around the circle logo are not part of my logo. My website emberhollowwicks.com and I am yet to develop it. Many thanks for helping with this design, and I look forward to receiving your ideas. On the package, I would like my Business Logo and a space to put the fragrance name (I will be getting a different colour box for each scent so they each stand out with their own separate identity. I would like this quote on the side or back of the box 'Every cloud has a silver lining' Thanks so much Janelle :-).

Target Market(s)

25-35 year olds

Industry/Entity Type

To be marketed to all types of shops, boutiques, clothing shops. homewares. To be bought by a consumer for a gift for themselves or a gift for family or friends.

Font styles to use
Script

Colors

Designer to choose colors to be used in the design.

Requirements
Must have
• Eye catching, dreamy, mesmorizing, mystical, eye catching packaging design. As I will be using a different coloured pack for each of my ten scents, need a design that can look good in any colours
Nice to have
• Use your artistic flair

```html
<!DOCTYPE html>
<html lang="en">
<head>
<meta charset="utf-8">
<title>Ember Hollow Candles – Earth Blend Packaging</title>
<link rel="stylesheet" href="https://fonts.googleapis.com/css2?family=Great+Vibes&family=Montserrat:wght@300;400;700&display=swap">
<style>
  :root {
    --page: #f4f4f4;
    --ink: #111111;
    --teal-deep: #07463f;
    --teal: #0a5a51;
    --teal-light: #0d6a5e;
    --gold: #b08a3e;
    --gold-soft: #8a7a3e;
    --silver: #e6ebe9;
    --aqua: #5fc4c4;
  }
  * { box-sizing: border-box; margin: 0; padding: 0; }
  html, body { width: 1200px; height: 907px; overflow: hidden; background: var(--page); }
  body { position: relative; font-family: "Montserrat", sans-serif; }

  .panel {
    position: absolute;
    overflow: hidden;
    box-shadow: 0 6px 18px rgba(0,0,0,0.12);
  }
  .panel-pattern {
    position: absolute; inset: 0;
    background:
      radial-gradient(circle at 30% 30%, rgba(176,138,62,0.35), transparent 60%),
      radial-gradient(circle at 75% 80%, rgba(176,138,62,0.3), transparent 55%),
      linear-gradient(135deg, var(--teal) 0%, #0c5c4c 50%, var(--teal-deep) 100%);
  }
  .medallion {
    position: absolute;
    border-radius: 50%;
    background: linear-gradient(100deg, var(--teal-deep) 0%, var(--teal) 55%, var(--teal-light) 100%);
    box-shadow: 0 4px 14px rgba(0,0,0,0.35);
    display: flex; flex-direction: column; align-items: center; justify-content: center;
    text-align: center;
  }

  /* box faces */
  .face-top   { left: 380px; top: 40px;  width: 300px; height: 300px; }
  .face-side  { left: 60px;  top: 380px; width: 300px; height: 300px; }
  .face-front { left: 380px; top: 380px; width: 300px; height: 300px; }

  .face-top .medallion { left: 40px; top: 60px; width: 220px; height: 180px; }
  .face-side .medallion { left: 30px; top: 30px; width: 240px; height: 240px; }
  .face-front .medallion { left: 25px; top: 25px; width: 250px; height: 250px; }

  .brand-ring {
    border: 1.5px solid var(--gold);
    border-radius: 50%;
    display: flex; flex-direction: column; align-items: center; justify-content: center;
  }
  .face-top .brand-ring { width: 190px; height: 150px; }
  .face-side .brand-ring { width: 110px; height: 130px; margin-bottom: 10px; }

  .brand-name {
    font-family: "Great Vibes", cursive;
    color: var(--gold);
    line-height: 1.05;
  }
  .face-top .brand-name { font-size: 30px; }
  .face-side .brand-name { font-size: 19px; }

  .brand-tagline {
    font-size: 6px; letter-spacing: 1px; color: var(--silver);
    text-transform: uppercase; margin-top: 6px;
  }
  .face-side .brand-tagline { font-size: 4.5px; }

  .quote {
    font-family: "Great Vibes", cursive;
    color: var(--silver);
    font-size: 19px;
    padding: 0 20px;
  }

  .product-name {
    font-family: "Great Vibes", cursive;
    color: var(--silver);
    line-height: 1;
  }
  .rule { height: 1px; background: var(--gold); }
  .fragrance {
    color: var(--silver); font-weight: 300; text-transform: uppercase;
  }
  .range-line {
    color: var(--silver); font-weight: 300; text-transform: uppercase;
  }

  .face-front .product-name { font-size: 46px; }
  .face-front .rule { width: 190px; margin: 6px 0 10px; }
  .face-front .fragrance { font-size: 8px; letter-spacing: 7px; }
  .face-front .range-line { font-size: 6px; letter-spacing: 3.5px; margin-top: 56px; }

  /* candle wrap label */
  .candle-label { left: 720px; top: 300px; width: 440px; height: 470px; }
  .candle-label .medallion { left: 25px; top: 40px; width: 390px; height: 390px; }
  .candle-label .product-name { font-size: 72px; }
  .candle-label .rule { width: 320px; margin: 10px 0 16px; }
  .candle-label .fragrance { font-size: 11px; letter-spacing: 10px; }
  .candle-label .range-line { font-size: 8px; letter-spacing: 5px; margin-top: 90px; }

  .face-caption {
    position: absolute;
    font-family: "Montserrat", sans-serif; font-weight: 700;
    font-size: 30px; color: var(--ink);
  }
  .caption-top   { left: 700px; top: 150px; }
  .caption-side  { left: 180px; top: 700px; }
  .caption-front { left: 490px; top: 700px; }
</style>
</head>
<body>

  <section class="panel face-top">
    <div class="panel-pattern" role="img" aria-label="Gold hand-drawn concentric arc pattern on deep teal"></div>
    <div class="medallion">
      <div class="brand-ring">
        <span class="brand-name">Ember Hollow<br>Candles</span>
        <span class="brand-tagline">Hand poured soy wax</span>
      </div>
    </div>
  </section>

  <section class="panel face-side">
    <div class="panel-pattern" role="img" aria-label="Gold hand-drawn concentric arc pattern on deep teal"></div>
    <div class="medallion">
      <div class="brand-ring">
        <span class="brand-name">Ember Hollow<br>Candles</span>
        <span class="brand-tagline">Hand poured soy wax</span>
      </div>
      <p class="quote">‘Every cloud has a silver lining’</p>
    </div>
  </section>

  <section class="panel face-front">
    <div class="panel-pattern" role="img" aria-label="Gold hand-drawn concentric arc pattern on deep teal"></div>
    <div class="medallion">
      <h1 class="product-name">Ember Hollow</h1>
      <div class="rule"></div>
      <p class="fragrance">Earth Blend</p>
      <p class="range-line">Handmade soy candles</p>
    </div>
  </section>

  <section class="panel candle-label">
    <div class="panel-pattern" role="img" aria-label="Gold hand-drawn concentric arc pattern on deep teal"></div>
    <div class="medallion">
      <h2 class="product-name">Ember Hollow</h2>
      <div class="rule"></div>
      <p class="fragrance">Earth Blend</p>
      <p class="range-line">Handmade soy candles</p>
    </div>
  </section>

  <span class="face-caption caption-top">top</span>
  <span class="face-caption caption-side">side</span>
  <span class="face-caption caption-front">front</span>

</body>
</html>
```